business card for 3D Printing online platform for new company

Need a business card aligned to my logo attached.

back should be logo on full side. colour should be blue background.

front should convey the following info with orange text (bold/similar font to logo) and white background. logo should be on 1/3 coverage (on blue background) of front side with following details laid out on remainder 2/3 of side (white background):

"Shaping Wonder Solid..." - text should be hand written to look like it has been written with a fountain pen effect and in quotes.

The following "email", "call" and "web" below should be of 3D format, whether it be an icon or the text in 3D.

Colin Pettigrew
Imagination Engineer

email :colin@brovalprint.com
call: +44 (0) 77812 30597
web: www.brovalprint.com

Thanks and good luck

Colin

thanks all for the submissions so far. there has been quite a few in a short space of time, but most have not addressed the brief that has been created. it must include the text as described and also I want some form of 3D design incorporated into the business card design.

thanks

colin

Business

Must have
• some form of 3D design whether it be the text (as requested above for the icons), or part of the card design.

```html
<!DOCTYPE html>
<html lang="en">
<head>
<meta charset="utf-8">
<title>Broval business card</title>
<link rel="stylesheet" href="https://fonts.googleapis.com/css2?family=Ubuntu:wght@400;500;700&family=Homemade+Apple&display=swap">
<style>
  :root {
    --stage: #b9babc;
    --blue: #1c5b90;
    --blue-deep: #114677;
    --blue-light: #2d74ab;
    --ink-blue: #1d5690;
    --orange: #f0891c;
    --yellow: #f5c41a;
    --paper: #f4f5f7;
    --paper-shade: #e4e6ea;
    --white: #ffffff;
  }
  * { box-sizing: border-box; margin: 0; padding: 0; }
  html, body {
    width: 1200px; height: 800px; overflow: hidden;
    background: var(--stage);
    font-family: "Ubuntu", sans-serif;
  }
  .canvas { position: relative; width: 1200px; height: 800px; }

  .card { position: absolute; overflow: hidden; box-shadow: 0 6px 18px rgba(0,0,0,.25); }
  .facets { position: absolute; inset: 0; }

  /* back */
  .card-back {
    left: 90px; top: 125px; width: 350px; height: 550px;
    background: linear-gradient(160deg, var(--blue-light), var(--blue) 45%, var(--blue-deep));
  }
  .back-mark {
    position: absolute; left: 50%; top: 50%;
    transform: translate(-50%, -50%);
    display: flex; align-items: center; gap: 16px;
  }
  .back-name {
    writing-mode: vertical-rl; transform: rotate(180deg);
    font-weight: 700; font-size: 46px; color: var(--white); letter-spacing: 1px;
  }
  .mark-circle {
    border-radius: 50%;
    background: radial-gradient(circle at 40% 35%, #3f8fd0, var(--blue-deep));
    border: 5px solid var(--orange);
    box-shadow: 0 0 0 3px var(--yellow);
  }
  .back-mark .mark-circle { width: 150px; height: 150px; }

  /* front */
  .card-front {
    left: 490px; top: 205px; width: 630px; height: 390px;
    background: linear-gradient(180deg, var(--paper), var(--paper-shade));
  }
  .front-brand {
    position: absolute; left: 0; top: 0; width: 100%; height: 132px;
    background: linear-gradient(160deg, var(--blue-light), var(--blue) 50%, var(--blue-deep));
  }
  .brand-row {
    position: absolute; left: 28px; top: 20px;
    display: flex; align-items: center; gap: 16px;
  }
  .brand-row .mark-circle { width: 62px; height: 62px; border-width: 3px; box-shadow: 0 0 0 2px var(--yellow); }
  .brand-name { font-weight: 700; font-size: 48px; color: var(--white); letter-spacing: 1px; }
  .tagline {
    position: absolute; left: 150px; top: 86px;
    font-family: "Homemade Apple", cursive;
    font-size: 20px; color: var(--white);
  }
  .accent-rule {
    position: absolute; left: 0; top: 132px; width: 100%; height: 6px;
    background: linear-gradient(90deg, var(--yellow), var(--orange));
  }
  .identity { position: absolute; left: 36px; top: 176px; }
  .person-name { font-weight: 700; font-size: 30px; color: var(--ink-blue); }
  .person-role { font-size: 18px; color: var(--ink-blue); margin-top: 6px; }
  .divider {
    position: absolute; left: 318px; top: 168px; width: 1px; height: 180px;
    background: var(--ink-blue); opacity: .6;
  }
  .contacts { position: absolute; left: 342px; top: 200px; list-style: none; }
  .contacts li {
    display: flex; align-items: center; gap: 12px;
    font-size: 21px; color: var(--ink-blue); margin-bottom: 14px;
  }
  .contact-icon { width: 30px; height: 30px; flex: none; }
</style>
</head>
<body>
<div class="canvas">

  <section class="card card-back" aria-label="Card back">
    <svg class="facets" viewBox="0 0 350 550" aria-hidden="true">
      <polygon points="0,0 350,0 350,140 0,60" fill="#ffffff" opacity=".06"/>
      <polygon points="0,60 350,140 350,230" fill="#ffffff" opacity=".05"/>
      <polygon points="0,430 350,300 350,550 0,550" fill="#000000" opacity=".08"/>
      <polygon points="0,480 190,550 0,550" fill="#ffffff" opacity=".06"/>
    </svg>
    <div class="back-mark">
      <span class="back-name">broval</span>
      <span class="mark-circle"></span>
    </div>
  </section>

  <section class="card card-front" aria-label="Card front">
    <div class="front-brand">
      <svg class="facets" viewBox="0 0 630 132" preserveAspectRatio="none" aria-hidden="true">
        <polygon points="0,0 630,0 630,40 0,90" fill="#ffffff" opacity=".05"/>
        <polygon points="380,132 630,60 630,132" fill="#000000" opacity=".08"/>
      </svg>
      <div class="brand-row">
        <span class="mark-circle"></span>
        <span class="brand-name">broval</span>
      </div>
      <p class="tagline">"Shaping Wonder Solid..."</p>
    </div>
    <div class="accent-rule"></div>

    <div class="identity">
      <p class="person-name">Colin Pettigrew</p>
      <p class="person-role">Imagination Engineer</p>
    </div>
    <div class="divider"></div>

    <svg width="0" height="0" aria-hidden="true" style="position:absolute">
      <defs>
        <radialGradient id="iconBall" cx="40%" cy="30%" r="70%">
          <stop offset="0" stop-color="#8cc4f0"/>
          <stop offset=".55" stop-color="#2d74ab"/>
          <stop offset="1" stop-color="#0d3c68"/>
        </radialGradient>
      </defs>
    </svg>

    <ul class="contacts">
      <li>
        <svg class="contact-icon" viewBox="0 0 30 30" aria-hidden="true">
          <circle cx="15" cy="15" r="14" fill="url(#iconBall)"/>
          <rect x="10" y="7" width="10" height="16" rx="2" fill="#fff"/>
          <rect x="12" y="9.5" width="6" height="8" fill="#2d74ab"/>
        </svg>
        <span>+44 (0) 77812 30597</span>
      </li>
      <li>
        <svg class="contact-icon" viewBox="0 0 30 30" aria-hidden="true">
          <circle cx="15" cy="15" r="14" fill="url(#iconBall)"/>
          <rect x="7.5" y="10" width="15" height="10" fill="#fff"/>
          <polyline points="7.5,10 15,16 22.5,10" fill="none" stroke="#2d74ab" stroke-width="1.4"/>
        </svg>
        <span>colin@brovalprint.com</span>
      </li>
      <li>
        <svg class="contact-icon" viewBox="0 0 30 30" aria-hidden="true">
          <circle cx="15" cy="15" r="14" fill="url(#iconBall)"/>
          <circle cx="15" cy="15" r="7.5" fill="none" stroke="#fff" stroke-width="1.6"/>
          <ellipse cx="15" cy="15" rx="3.2" ry="7.5" fill="none" stroke="#fff" stroke-width="1.3"/>
          <line x1="7.5" y1="15" x2="22.5" y2="15" stroke="#fff" stroke-width="1.3"/>
        </svg>
        <span>www.brovalprint.com</span>
      </li>
    </ul>
  </section>

</div>
</body>
</html>
```